Radiant Harvest Gathering 2021

I am looking to create a flyer for a one day prayer retreat our church is organizing. This flyer will be posted on social media, websites, mobile apps, and will also be printed so it can be mailed to people.

I am looking for something professional, with good use of our logo and band colors (logo colors).

I am counting on the designer's skill, creativity, art and knowledge of media communication to produce a flyer that will effectively and quickly convey the message we are trying to spread.

CONTENT OF THE FLYER:
Event title: Radiant Harvest Gathering
Date: Tuesday July 2nd, 2021
Time: 11:00AM - 7:00PM
Bellmore Hotel, 4817 Wexley Avenue, Portland, Maine 04109 (Room: Tamarind)
Event Key words to highlight what the event is about: Prayer, Fasting, Worship, Prophecy, Revival.
Key phrases:
A one day prayer retreat.
Jesus Chris is Lord

Contact info:
www.quvello.org
Phone: 207 555 0148
Email: contact@brookmeadow.org

```html
<!DOCTYPE html>
<html lang="en">
<head>
<meta charset="utf-8">
<title>Radiant Harvest Gathering 2021</title>
<link rel="stylesheet" href="https://fonts.googleapis.com/css2?family=Pacifico&family=Questrial&display=swap">
<style>
  :root {
    --page: #ffffff;
    --navy: #0f3560;
    --navy-deep: #0b2847;
    --maroon: #762f33;
    --maroon-dark: #4a1c20;
    --blush: #f6d9cf;
    --gold: #f2e200;
    --white: #ffffff;
    --photo-light: #f1f2f4;
    --photo-mid: #9a8f8c;
    --photo-warm: #9b3a35;
    --photo-dark: #5a2426;
  }
  * { box-sizing: border-box; margin: 0; padding: 0; }
  html, body { width: 1200px; height: 891px; overflow: hidden; background: var(--page); }
  .canvas { position: relative; width: 1200px; height: 891px; background: var(--page); }

  .flyer {
    position: absolute; left: 305px; top: 30px; width: 590px; height: 830px;
    overflow: hidden; font-family: "Questrial", sans-serif;
    box-shadow: 0 10px 30px rgba(0,0,0,0.18);
  }
  .flyer__photo {
    position: absolute; inset: 0;
    background:
      radial-gradient(ellipse 45% 35% at 62% 58%, #d9a98f 0%, rgba(217,169,143,0) 70%),
      radial-gradient(ellipse 60% 50% at 95% 55%, var(--photo-warm) 0%, rgba(155,58,53,0) 75%),
      linear-gradient(160deg, var(--photo-light) 0%, #d7d7d9 30%, var(--photo-mid) 52%, var(--photo-dark) 80%);
  }
  .flyer__shape { position: absolute; inset: 0; width: 590px; height: 830px; }

  .flyer__title {
    position: absolute; left: 40px; top: 40px; width: 420px;
    font-family: "Pacifico", cursive; color: var(--navy);
    font-size: 56px; line-height: 76px;
  }
  .flyer__title span { display: block; }
  .flyer__title span:nth-child(1) { padding-left: 36px; }
  .flyer__title span:nth-child(2) { padding-left: 18px; }

  .flyer__info {
    position: absolute; left: 20px; top: 590px; width: 340px;
    text-align: center; color: var(--white);
  }
  .flyer__tagline { font-size: 22px; line-height: 26px; letter-spacing: 0.3px; }
  .flyer__details { margin-top: 8px; color: var(--gold); font-size: 13.5px; line-height: 17px; }

  .flyer__keywords {
    position: absolute; left: 0; top: 750px; width: 590px;
    text-align: center; color: var(--white); font-size: 19px; letter-spacing: 0.5px;
  }
  .flyer__contact {
    position: absolute; left: 0; top: 790px; width: 590px; height: 26px;
    background: var(--blush); color: var(--maroon);
    font-size: 12.5px; line-height: 26px; text-align: center;
  }

  .brand {
    position: absolute; left: 398px; top: 585px; width: 150px; height: 150px;
    background: var(--navy); display: flex; align-items: center; justify-content: center;
    border-bottom: 18px solid var(--navy-deep);
  }
  .brand__name { color: var(--white); font-size: 26px; letter-spacing: 1px; }
</style>
</head>
<body>
<div class="canvas">
  <article class="flyer">
    <div class="flyer__photo" role="img" aria-label="Photo of clasped hands in prayer against a soft blurred background, person wearing a red knit sweater"></div>

    <svg class="flyer__shape" viewBox="0 0 590 830" aria-hidden="true">
      <polygon points="0,472 300,654 590,654 590,830 0,830" fill="var(--maroon-dark)" opacity="0.55"/>
      <polygon points="0,478 300,660 590,660 590,830 0,830" fill="var(--maroon)"/>
    </svg>

    <h1 class="flyer__title">
      <span>Radiant</span>
      <span>Harvest</span>
      <span>Gathering</span>
    </h1>

    <div class="flyer__info">
      <p class="flyer__tagline">A one day prayer retreat.<br>Jesus Chris is Lord</p>
      <p class="flyer__details">Tuesday July 2nd, 2021 | 11:00AM - 7:00PM<br>Bellmore Hotel, 4817 Wexley Avenue, Portland,<br>Maine 04109 (Room: Tamarind)</p>
    </div>

    <div class="brand"><span class="brand__name">QUVELLO</span></div>

    <p class="flyer__keywords">Prayer, | Fasting, | Worship | Prophecy | Revival.</p>
    <p class="flyer__contact">www.quvello.org &nbsp;|&nbsp; Phone: 207 555 0148 &nbsp;|&nbsp; Email: contact@brookmeadow.org</p>
  </article>
</div>
</body>
</html>
```